Coffee Stop sign

"Rise and Grind" is the catch phrase for this little coffee stop.
This will be a two sided (printed on reflective alumaboard probably) sign that sits flat out on the ground in front of the store. We serve French Press and drip coffee to go.
The sign will be approx. 4' tall, and 2-3' wide.
One of the ideas for this sign is a hand coming out of the ground in front of a tombstone grasping a coffee cup..
there is a lot of room for designer discretion.
Early morning and in a rush crowd..
Store

```html
<!DOCTYPE html>
<html lang="en">
<head>
<meta charset="utf-8">
<title>Early Bird Coffee Shop – French Press and Drip Coffee</title>
<link href="https://fonts.googleapis.com/css2?family=Playball&family=Josefin+Sans:wght@300&display=swap" rel="stylesheet">
<style>
  :root {
    --night-roast: #160b05;
    --dark-roast: #24140a;
    --wood-shadow: #4a2d15;
    --wood-warm: #7a4f27;
    --wood-glow: #8f6033;
    --crema: #8c5c34;
    --crema-light: #a3744a;
    --espresso-ink: #1d130c;
    --cup-dark: #2a1a10;
    --cup-mid: #5b3f2a;
    --saucer: #9a8470;
  }
  * { margin: 0; padding: 0; box-sizing: border-box; }
  html, body { width: 900px; height: 1200px; overflow: hidden; background: var(--night-roast); }
  .sign {
    position: relative;
    width: 900px;
    height: 1200px;
    overflow: hidden;
    background:
      radial-gradient(ellipse 520px 420px at 450px 860px, var(--wood-glow) 0%, var(--wood-warm) 45%, transparent 100%),
      linear-gradient(180deg, var(--night-roast) 0%, var(--dark-roast) 40%, var(--wood-shadow) 55%, var(--wood-warm) 75%, var(--wood-shadow) 100%);
  }
  .menu-title {
    position: absolute;
    top: 58px;
    left: 0;
    width: 900px;
    text-align: center;
    font-family: "Playball", cursive;
    color: var(--crema);
    text-shadow: 0 3px 4px rgba(0,0,0,0.7);
  }
  .menu-title .line {
    display: block;
    margin: 0 auto;
    line-height: 1;
    border-bottom: 2px solid var(--crema);
    box-shadow: 0 2px 2px -1px rgba(0,0,0,0.6);
  }
  .menu-title .line-1 { width: 320px; font-size: 60px; padding-bottom: 10px; }
  .menu-title .line-2 { width: 316px; font-size: 50px; padding: 22px 0 14px; }
  .menu-title .line-3 { width: 325px; font-size: 60px; padding: 22px 0 10px; }
  .cup-photo {
    position: absolute;
    left: 236px;
    top: 600px;
    width: 394px;
    height: 420px;
    border-radius: 50%;
    background: radial-gradient(circle at 48% 38%, var(--cup-mid) 0%, var(--cup-dark) 38%, var(--saucer) 62%, var(--wood-warm) 78%, transparent 100%);
    opacity: 0.9;
  }
  .shop-name {
    position: absolute;
    left: 234px;
    top: 1040px;
    width: 400px;
    font-family: "Josefin Sans", sans-serif;
    font-weight: 300;
    color: var(--espresso-ink);
    text-align: right;
  }
  .shop-name .tagline {
    display: block;
    font-size: 30px;
    letter-spacing: 2px;
    padding-right: 6px;
  }
  .shop-name .store {
    display: block;
    font-size: 56px;
    letter-spacing: 4px;
    line-height: 1.05;
    text-align: left;
    border-bottom: 2px solid var(--espresso-ink);
    padding-bottom: 4px;
  }
</style>
</head>
<body>
  <main class="sign">
    <h1 class="menu-title">
      <span class="line line-1">French Press</span>
      <span class="line line-2">and</span>
      <span class="line line-3">Drip Coffee</span>
    </h1>
    <div class="cup-photo" role="img" aria-label="Photo of a cup of black coffee on a saucer, seen from above, with a butterfly shape in the crema"></div>
    <div class="shop-name">
      <span class="tagline">EARLY BIRD</span>
      <span class="store">COFFEE SHOP</span>
    </div>
  </main>
</body>
</html>
```